Heritage Depot Business Cards

Require a business card design. <br/><br/>Needs to include logo (either round or long version) plus these details:<br/>Maya Corvell<br/>Heritage Depot<br/>maya@brightmarttrade.com.au<br/>02 6418 7395<br/>PO Box Glenfarrow NSW 2791<br/>www.heritagedepot.com.au<br/><br/>I need in an editable format so that I can create for multiple staff members. <br/><br/>

Target Market(s)

We are an online store selling renovation products to home owners are builders. Looking for a classic classy design.

Industry/Entity Type

Home And Garden

Contact Information for Business Card

Maya Corvell
Heritage Depot
maya@brightmarttrade.com.au
02 6418 7395
PO Box Glenfarrow NSW 2791
www.heritagedepot.com.au

Colors

Designer to choose colors to be used in the design.

Requirements
Must have
• Must include Logo.

```html
<!DOCTYPE html>
<html lang="en">
<head>
<meta charset="utf-8">
<title>Heritage Depot Business Cards</title>
<link href="https://fonts.googleapis.com/css2?family=Lato:wght@400&display=swap" rel="stylesheet">
<style>
  :root {
    --canvas: #f0f0f0;
    --paper: #ffffff;
    --ink: #05080a;
    --light: #ffffff;
  }
  * { margin: 0; padding: 0; box-sizing: border-box; }
  html, body { width: 1200px; height: 1000px; overflow: hidden; }
  body {
    background: var(--canvas);
    font-family: 'Lato', Arial, sans-serif;
    position: relative;
  }
  .card {
    position: absolute;
    left: 324px;
    width: 549px;
    background: var(--paper);
    overflow: hidden;
  }
  .card-front { top: 108px; height: 368px; }
  .card-back { top: 524px; height: 368px; }
  .band {
    position: absolute;
    left: 0; right: 0; bottom: 0;
    background: var(--ink);
  }
  .card-front .band { top: 219px; }
  .card-back .band { top: 132px; }
  .brand {
    position: absolute;
    display: flex;
    align-items: center;
    color: var(--ink);
    white-space: nowrap;
  }
  .brand-mark {
    border: 1.5px solid var(--ink);
    border-radius: 50%;
    flex: none;
  }
  .card-front .brand { left: 134px; top: 100px; font-size: 30px; gap: 14px; }
  .card-front .brand-mark { width: 72px; height: 72px; }
  .card-back .brand { left: 54px; top: 46px; font-size: 18px; gap: 8px; }
  .card-back .brand-mark { width: 42px; height: 42px; }
  .website {
    position: absolute;
    left: 0; right: 0; top: 283px;
    text-align: center;
    color: var(--light);
    font-size: 17px;
  }
  .person {
    position: absolute;
    left: 64px; top: 160px;
    color: var(--light);
    font-size: 30px;
  }
  .contacts {
    position: absolute;
    left: 66px; top: 218px;
    list-style: none;
    color: var(--light);
    font-size: 23px;
  }
  .contacts li {
    display: flex;
    align-items: center;
    gap: 8px;
    height: 37px;
  }
  .contacts svg { width: 29px; height: 29px; flex: none; margin-top: 6px; }
</style>
</head>
<body>
  <section class="card card-front">
    <div class="brand"><span class="brand-mark"></span><span class="brand-name">Heritage Depot</span></div>
    <div class="band"></div>
    <p class="website">www.heritagedepot.com.au</p>
  </section>

  <section class="card card-back">
    <div class="brand"><span class="brand-mark"></span><span class="brand-name">Heritage Depot</span></div>
    <div class="band"></div>
    <h1 class="person" style="font-weight:400">Maya Corvell</h1>
    <ul class="contacts">
      <li>
        <svg viewBox="0 0 30 30" fill="none" stroke="#fff" stroke-width="2"><circle cx="15" cy="15" r="13"/><rect x="8" y="10" width="14" height="10"/><path d="M8 10l7 6 7-6"/></svg>
        <span>maya@brightmarttrade.com.au</span>
      </li>
      <li>
        <svg viewBox="0 0 30 30" fill="none" stroke="#fff" stroke-width="2"><circle cx="15" cy="15" r="13"/><path d="M20 8c-4 0-10 6-10 12l2 2 3-3-2-2c0-3 3-6 6-6l2 2 3-3z" fill="#fff" stroke="none"/></svg>
        <span>02 6418 7395</span>
      </li>
      <li>
        <svg viewBox="0 0 30 30" fill="none" stroke="#fff" stroke-width="2"><circle cx="15" cy="15" r="13"/><path d="M8 15l7-6 7 6h-2v6h-4v-4h-2v4h-4v-6z" fill="#fff" stroke="none"/></svg>
        <span>PO Box Glenfarrow NSW 2791</span>
      </li>
    </ul>
  </section>
</body>
</html>
```